Laminated Training Card; highly professional yet engaging, colorful, fits branding

We need an 8 1/2" x 11" piece, printed front and back, to inspire and offer instructions for nonprofit leaders on key coaching skills to use with their staff. Though it's in a professional services setting, this piece communicates a sense of fun and excitement to encourage leaders to try out these skills, and keep the training card close at hand. An infographic style would be ideal.

Target Market(s)

Nonprofit leaders will use the laminated training card in a face to face training class, and then take it back to the office to use to 'train' their staff

Industry/Entity Type

Training

Font styles to use
Serif

Requirements
Must have
• See project brief attached
Nice to have
Should not have

```html
<!DOCTYPE html>
<html lang="en">
<head>
<meta charset="utf-8">
<title>Accountability Culture Training Card</title>
<link href="https://fonts.googleapis.com/css2?family=Tinos:wght@400;700&family=Questrial&display=swap" rel="stylesheet">
<style>
  :root {
    --sky: #a9dcee;
    --paper: #e6e7e8;
    --slate: #4d4d4f;
    --lime: #8dc63f;
    --orange: #d9532b;
    --blue: #8ed0e8;
    --olive: #a9c23c;
    --ink: #231f20;
    --white: #ffffff;
    --brown: #6e4b39;
    --grey-text: #58595b;
  }
  * { box-sizing: border-box; margin: 0; padding: 0; }
  html, body { width: 927px; height: 1200px; overflow: hidden; }
  body {
    position: relative;
    background: var(--paper);
    font-family: "Tinos", "Times New Roman", serif;
    color: var(--white);
  }
  .masthead {
    position: absolute; left: 0; top: 0; width: 927px; height: 92px;
    background: var(--sky);
    display: flex; align-items: center; justify-content: center; gap: 14px;
  }
  .brand-dot {
    width: 52px; height: 52px; border-radius: 50%; background: var(--brown); flex: none;
  }
  .brand-name {
    font-family: "Tinos", serif; font-weight: 700; color: var(--brown);
    font-size: 27px; line-height: 1.05;
  }
  .brand-name small { display: block; font-size: 21px; font-weight: 700; }
  .title-band {
    position: absolute; left: 0; top: 94px; width: 927px; height: 72px;
    background: var(--slate); text-align: center;
    font-weight: 700; text-transform: uppercase; font-size: 24.5px; line-height: 1.3;
    padding-top: 6px; letter-spacing: 0.2px;
  }
  .title-band .bullet { color: var(--lime); }
  .tip { position: absolute; }
  .tip-questions {
    left: 20px; top: 178px; width: 907px; height: 312px;
    background: var(--orange); border-radius: 150px 0 0 150px;
  }
  .tip-dimensions {
    left: 0; top: 508px; width: 905px; height: 320px;
    background: var(--blue); border-radius: 0 150px 150px 0;
  }
  .tip-toxins {
    left: 20px; top: 842px; width: 907px; height: 316px;
    background: var(--olive); border-radius: 150px 0 0 150px;
  }
  .icon-badge {
    position: absolute; width: 186px; height: 186px; border-radius: 50%; background: var(--ink);
  }
  .tip-questions .icon-badge { left: 58px; top: 20px; }
  .tip-dimensions .icon-badge { left: 662px; top: 8px; }
  .tip-toxins .icon-badge { left: 58px; top: 20px; }
  .tip-heading {
    position: absolute; color: var(--ink); font-weight: 700; font-size: 24px;
  }
  .tip-questions .tip-heading { left: 308px; top: 24px; }
  .tip-dimensions .tip-heading { left: 345px; top: 24px; }
  .tip-toxins .tip-heading { left: 324px; top: 28px; }
  .tip-body {
    position: absolute; font-weight: 700; font-size: 16.6px; line-height: 1.22;
  }
  .tip-body p + p { margin-top: 19px; }
  .tip-questions .tip-body { left: 263px; top: 64px; width: 630px; }
  .tip-dimensions .tip-body { left: 55px; top: 76px; width: 600px; font-size: 16px; }
  .tip-toxins .tip-body { left: 320px; top: 68px; width: 570px; }
  .antidotes { list-style: none; }
  .antidotes li { padding-left: 22px; text-indent: -22px; }
  .antidotes li::before { content: "-\00a0\00a0"; }
  .footer {
    position: absolute; left: 0; top: 1160px; width: 927px; height: 40px;
    font-family: "Questrial", sans-serif; color: var(--grey-text); font-size: 14px; line-height: 1.2;
  }
  .footer-brand {
    position: absolute; left: 58px; top: 4px; display: flex; align-items: center; gap: 6px;
  }
  .footer-brand .brand-dot { width: 20px; height: 20px; }
  .footer-brand .brand-name { font-size: 15px; }
  .footer-brand .brand-name small { font-size: 11px; }
  .footer-contact { position: absolute; left: 285px; top: 4px; width: 360px; text-align: center; }
  .footer-status { position: absolute; left: 690px; top: 4px; width: 200px; text-align: center; }
</style>
</head>
<body>
  <header class="masthead">
    <span class="brand-dot"></span>
    <div class="brand-name">Northpath Center<small>for Nonprofit Leadership</small></div>
  </header>

  <h1 class="title-band">Create an Accountability Culture with Teams and Allies<br>
    <span class="bullet">•</span>Valuable Tips for Success<span class="bullet">•</span></h1>

  <section class="tip tip-questions">
    <div class="icon-badge" role="img" aria-label="Icon of a person with a speech bubble"></div>
    <h2 class="tip-heading">#1. Powerful Questions</h2>
    <div class="tip-body">
      <p>Coach yourself asking powerful questions; they break your internal monologue. Ask others a powerful question — that you don’t answer. They will feel deeply heard.</p>
      <p>Dream one moment: What’s possible? And establish accountability the next: What should I do when you miss your deadline?</p>
      <p>Asking questions isn’t reserved for the leader. Whoever asks the powerful questions is the leader in the moment.</p>
      <p>With whom is it safe to ask powerful questions in your culture?</p>
    </div>
  </section>

  <section class="tip tip-dimensions">
    <div class="icon-badge" role="img" aria-label="Icon of a person holding a flag"></div>
    <h2 class="tip-heading">#2. 4 Dimensions of Leadership</h2>
    <div class="tip-body">
      <p>Knowing when to move between these stances = leadership mastery.</p>
      <p>Leading from the front: eyes on the vision and staying connected to those who follow<br>
      Leading from the side: locking arms in the company of equals. Eyes on the shared vision, but each has their own path to get there.<br>
      Leading from behind: ‘fading’ while still holding the space. You’ve got their backs.<br>
      Leading from above: seeing the big picture.</p>
    </div>
  </section>

  <section class="tip tip-toxins">
    <div class="icon-badge" role="img" aria-label="Icon of a person with a magnifying glass"></div>
    <h2 class="tip-heading">#3. 4 Team Toxins</h2>
    <div class="tip-body">
      <p>Defensiveness, blaming, stonewalling and contempt. We all do it, especially when stress is high. There’s camaraderie through complaining. But left unchecked, great work comes to a halt.</p>
      <p>Antidotes:</p>
      <ul class="antidotes">
        <li>Ask: what are you defending? What am I protecting? How can we keep this from spreading?</li>
        <li>Toxins can flood us. Take a break and come back to the conversation.</li>
        <li>Check assumptions. ‘I assume you have money in your budget. I assume you don’t want to be involved. I assume you’re supporting me on this.’</li>
      </ul>
    </div>
  </section>

  <footer class="footer">
    <div class="footer-brand">
      <span class="brand-dot"></span>
      <div class="brand-name">Northpath Center<small>for Nonprofit Leadership</small></div>
    </div>
    <div class="footer-contact">210 Harbor Ave, Suite 410 | Riverton, GA 30399<br>555-014-2270 | hello@northpathcenter.org</div>
    <div class="footer-status">501(c)(3) organization<br>funded by donations</div>
  </footer>
</body>
</html>
```